Corvale Real Estate

I manage 2 firms. The first one is Felmont and the logo is in blue (see the file) but i need a design for my business card for the second firm called CORVALE IMMOBILIER. This one is in charge of Real estate developer.

Colors
3176b5

```html
<!DOCTYPE html>
<html lang="fr">
<head>
<meta charset="utf-8">
<title>Corvale Immobilier – Business Card</title>
<link href="https://fonts.googleapis.com/css2?family=Lato:wght@400;700;900&display=swap" rel="stylesheet">
<style>
  :root {
    --brand-blue: #3a58a8;
    --ink: #2b2b2b;
    --muted-grey: #8a8a8a;
    --band-grey: #a9a9ab;
    --card-white: #ffffff;
    --backdrop: #d9dadc;
    --faint-blue: #e6eaf3;
  }
  * { margin: 0; padding: 0; box-sizing: border-box; }
  html, body { width: 1200px; height: 800px; overflow: hidden; }
  body {
    background: var(--backdrop);
    font-family: "Lato", sans-serif;
    position: relative;
  }
  .card {
    position: absolute;
    top: 250px;
    width: 520px;
    height: 300px;
    overflow: hidden;
    box-shadow: 0 6px 18px rgba(0,0,0,0.18);
  }
  /* Front */
  .card-front { left: 50px; background: var(--card-white); }
  .faint-block {
    position: absolute;
    right: 30px; top: 90px;
    width: 170px; height: 170px;
    background: var(--faint-blue);
  }
  .brand {
    position: absolute;
    left: 34px; top: 32px;
    display: flex; align-items: center; gap: 14px;
  }
  .brand-square {
    width: 34px; height: 34px;
    background: var(--brand-blue);
  }
  .brand-divider { width: 1px; height: 42px; background: var(--muted-grey); }
  .brand-name {
    color: var(--brand-blue);
    font-weight: 700;
    line-height: 1;
  }
  .brand-name .main { display: block; font-size: 32px; letter-spacing: 1px; }
  .brand-name .sub { display: block; font-size: 11px; letter-spacing: 7px; margin-top: 3px; }
  .contact {
    position: absolute;
    left: 96px; top: 108px;
    color: var(--ink);
    font-size: 14px;
    line-height: 1.3;
  }
  .person-name { color: var(--brand-blue); font-weight: 900; font-size: 19px; }
  .person-title { font-size: 14px; }
  .rule { width: 30px; height: 1px; background: var(--muted-grey); margin: 12px 0 14px; }
  .address { margin-bottom: 4px; }
  .contact-line { display: flex; align-items: center; gap: 6px; }
  .contact-line svg { width: 12px; height: 12px; flex: none; }
  .footer-band {
    position: absolute; left: 0; right: 0; bottom: 0; height: 16px;
    display: flex;
  }
  .footer-band .grey { width: 120px; background: var(--band-grey); }
  .footer-band .gap { width: 3px; background: var(--card-white); }
  .footer-band .blue { flex: 1; background: var(--brand-blue); }
  /* Back */
  .card-back { left: 630px; background: var(--brand-blue); color: var(--card-white); }
  .back-brand {
    position: absolute; left: 0; right: 0; top: 105px;
    display: flex; justify-content: center; align-items: center; gap: 14px;
  }
  .back-brand .brand-square { background: var(--card-white); width: 30px; height: 30px; }
  .back-brand .brand-name { color: var(--card-white); }
  .back-url {
    position: absolute; left: 0; right: 0; bottom: 48px;
    text-align: center; font-size: 13px; letter-spacing: 2px;
  }
</style>
</head>
<body>
  <section class="card card-front">
    <div class="faint-block"></div>
    <div class="brand">
      <div class="brand-square"></div>
      <div class="brand-divider"></div>
      <div class="brand-name"><span class="main">CORVALE</span><span class="sub">IMMOBILIER</span></div>
    </div>
    <div class="contact">
      <div class="person-name">Julien Marchal</div>
      <div class="person-title">Managing Director</div>
      <div class="rule"></div>
      <div class="address">27 Rue des Tanneurs<br>75011 Paris</div>
      <div class="contact-line">
        <svg viewBox="0 0 24 24"><path fill="#3a58a8" d="M6.6 10.8a15 15 0 0 0 6.6 6.6l2.2-2.2c.3-.3.7-.4 1-.2 1.1.4 2.3.6 3.6.6.6 0 1 .4 1 1V20c0 .6-.4 1-1 1A17 17 0 0 1 3 4c0-.6.4-1 1-1h3.5c.6 0 1 .4 1 1 0 1.3.2 2.5.6 3.6.1.3 0 .7-.2 1z"/></svg>
        <span>041 582 3067</span>
      </div>
      <div class="contact-line">
        <svg viewBox="0 0 24 24"><rect x="2" y="5" width="20" height="14" fill="none" stroke="#3a58a8" stroke-width="2"/><path d="M2 5l10 8 10-8" fill="none" stroke="#3a58a8" stroke-width="2"/></svg>
        <span>julien@corvaleimmobilier.fr</span>
      </div>
      <div class="contact-line">
        <svg viewBox="0 0 24 24"><circle cx="12" cy="12" r="9" fill="none" stroke="#3a58a8" stroke-width="2"/><path d="M3 12h18M12 3c3 3 3 15 0 18M12 3c-3 3-3 15 0 18" fill="none" stroke="#3a58a8" stroke-width="1.6"/></svg>
        <span>www.corvaleimmobilier.fr</span>
      </div>
    </div>
    <div class="footer-band"><div class="grey"></div><div class="gap"></div><div class="blue"></div></div>
  </section>

  <section class="card card-back">
    <div class="back-brand">
      <div class="brand-square"></div>
      <div class="brand-name"><span class="main">CORVALE</span><span class="sub">IMMOBILIER</span></div>
    </div>
    <div class="back-url">www.corvaleimmobilier.fr</div>
  </section>
</body>
</html>
```